Corewise Motion Business Cards

Can all designers please apply the following info on their designs' back-side of the business card: (please see brief file upload ('Info for backside...' - for required info, colours & layout)

SPECIALISING IN INDIVIDUAL PILATES INSTRUCTION
MATWORK – including small apparatus
and STUDIO:
VIVANTE 5 REFORMER
LADDER BARREL
MERIDAN BARREL
TENDRA DOME
KALVO CHAIR
TOR-I-VAN

Business Cards for Corewise Motion - applying the Corewise Motion logo design selected earlier.
Note the business card requires both a front and back side. Please refer to two uploaded ppt-files for type of info required to be displayed, and rough position of where info could be. Require innovative / fresh approach to business card design and use of colour by designers now. Please refer to and use logo as uploaded - also for potential business card colour application.

Dear Designers,

Please note the additional inclusion / upload of two draft ppt-files that try to show where I want what type of information, for both the front & back sides of the required business card, plus an attempt at showing the high-level concept / idea of business info position.

As my 'drafts' obviously lack colour and any ability towards innovative card design or approach – I now rely on your vastly superior graphic design abilities to produce a really great business card for my business…

Looking forward to your submissions!

Kind regards, Maren for: Corewise Motion 

Hello all Designers,

Can all designers please apply the following info on their designs' back-side of the business card: (please see / refer to the Brief and specifically the file upload ('Info for backside...' - for required info, colours & layout) - for the backside of the business card).

Info content (without colour, layout etc.):

and STUDIO:

VIVANTE 5 REFORMER

LADDER BARREL

MERIDAN BARREL

TENDRA DOME

KALVO CHAIR

TOR-I-VAN

Thank you to all designers that submitted for consideration!

With regards,

Corewise Motion

```html
<!DOCTYPE html>
<html lang="en">
<head>
<meta charset="utf-8">
<title>Corewise Motion – Business Card</title>
<link rel="stylesheet" href="https://fonts.googleapis.com/css2?family=Raleway:wght@400;600;700&family=Josefin+Sans:ital,wght@1,600&display=swap">
<style>
  :root {
    --orange: #ee8a1f;
    --orange-deep: #e2541e;
    --green: #8cc63f;
    --green-dark: #3f6b22;
    --white: #ffffff;
    --bg: #e9e7e3;
    --ink: #4a4a4a;
  }
  * { box-sizing: border-box; margin: 0; padding: 0; }
  html, body { width: 1200px; height: 900px; overflow: hidden; background: var(--bg); }
  body { position: relative; font-family: "Raleway", sans-serif; }

  .card {
    position: absolute;
    width: 525px; height: 300px;
    border-radius: 18px;
    background: var(--white);
    overflow: hidden;
    box-shadow: 0 6px 18px rgba(0,0,0,.18);
  }

  /* Back side */
  .card-back { left: 80px; top: 100px; }
  .card-back .side-bar {
    position: absolute; left: 0; top: 0; bottom: 0; width: 30px;
    background: var(--orange);
  }
  .card-back .headline {
    position: absolute; left: 52px; top: 30px;
    font-size: 13.5px; font-weight: 700; letter-spacing: .3px;
    color: var(--orange);
  }
  .card-back .services {
    position: absolute; left: 90px; top: 62px; width: 250px;
    color: var(--green-dark); font-size: 14px; line-height: 1.28; text-align: center;
  }
  .card-back .services ul { list-style: none; margin-top: 2px; }
  .card-back .services li::before {
    content: ""; display: inline-block; width: 7px; height: 7px; border-radius: 50%;
    background: var(--orange); margin-right: 8px; vertical-align: middle;
  }
  .card-back .mark-dot {
    position: absolute; right: 40px; top: 78px;
    width: 120px; height: 120px; border-radius: 50%;
    background: var(--green-dark);
  }

  /* Front side */
  .card-front { left: 595px; top: 480px; }
  .card-front .bands { position: absolute; inset: 0; }
  .card-front .brand {
    position: absolute; left: 60px; top: 26px;
    display: flex; align-items: center; gap: 12px;
  }
  .card-front .brand-dot { width: 34px; height: 34px; border-radius: 50%; background: var(--green-dark); }
  .card-front .brand-name { font-size: 34px; font-weight: 400; color: var(--orange-deep); }
  .card-front .person {
    position: absolute; left: 150px; top: 88px; color: var(--white);
  }
  .card-front .person-name { font-size: 16px; font-weight: 700; letter-spacing: .4px; }
  .card-front .person-title { font-size: 8.5px; margin-top: 4px; }
  .card-front .contacts {
    position: absolute; right: 60px; top: 140px;
    list-style: none; font-size: 11px; color: var(--white); line-height: 1.45;
  }
  .card-front .contacts li { display: flex; align-items: center; gap: 10px; }
  .card-front .contacts svg { width: 10px; height: 10px; fill: var(--orange-deep); }
  .card-front .address {
    position: absolute; left: 40px; top: 200px;
    display: flex; gap: 8px; color: var(--white); font-size: 11.5px; font-weight: 600; line-height: 1.3;
  }
  .card-front .address svg { width: 10px; height: 14px; fill: var(--orange-deep); margin-top: 1px; }
  .card-front .tagline {
    position: absolute; left: 0; right: 0; bottom: 18px; text-align: center;
    font-family: "Josefin Sans", sans-serif; font-style: italic; font-weight: 600;
    font-size: 16px; letter-spacing: 2.5px; color: var(--green-dark);
  }
</style>
</head>
<body>

<section class="card card-back" aria-label="Business card back">
  <div class="side-bar"></div>
  <h2 class="headline">SPECIALISING IN INDIVIDUAL PILATES INSTRUCTION</h2>
  <div class="services">
    <p>MATWORK – including small apparatus</p>
    <p>and STUDIO:</p>
    <ul>
      <li>VIVANTE 5 REFORMER</li>
      <li>LADDER BARREL</li>
      <li>MERIDAN BARREL</li>
      <li>TENDRA DOME</li>
      <li>KALVO CHAIR</li>
      <li>TOR-I-VAN</li>
    </ul>
  </div>
  <div class="mark-dot"></div>
</section>

<section class="card card-front" aria-label="Business card front">
  <svg class="bands" viewBox="0 0 525 300" preserveAspectRatio="none" aria-hidden="true">
    <path d="M0 95 C120 85 300 90 525 60 L525 170 C380 175 200 175 0 190 Z" fill="var(--orange)"/>
    <path d="M0 190 C150 178 330 172 525 160 L525 240 L0 250 Z" fill="var(--green)"/>
    <path d="M30 60 C70 90 70 150 30 190 C60 150 60 100 30 60 Z" fill="var(--green)"/>
    <path d="M420 110 C460 90 500 80 525 70 L525 110 C490 110 455 112 420 110 Z" fill="var(--green)"/>
    <path d="M140 200 C220 180 300 185 380 205 C300 195 220 195 140 200 Z" fill="var(--orange)"/>
  </svg>
  <div class="brand">
    <span class="brand-dot"></span>
    <span class="brand-name">Corewise Motion</span>
  </div>
  <div class="person">
    <h1 class="person-name">Maren Holloway</h1>
    <p class="person-title">Diploma of Professional Pilates Instruction</p>
  </div>
  <ul class="contacts">
    <li><svg viewBox="0 0 10 10"><rect x="2" y="0" width="6" height="10" rx="1.2"/></svg>040 123 4567</li>
    <li><svg viewBox="0 0 10 10"><rect x="0" y="2" width="10" height="7" rx="1"/></svg>info@corewisemotion.com</li>
    <li><svg viewBox="0 0 10 10"><path d="M5 0 L10 5 L8.5 5 L8.5 10 L1.5 10 L1.5 5 L0 5 Z"/></svg>www.corewisemotion.com.au</li>
  </ul>
  <address class="address">
    <svg viewBox="0 0 10 14"><path d="M5 0 C2 0 0 2 0 5 C0 8 5 14 5 14 C5 14 10 8 10 5 C10 2 8 0 5 0 Z"/></svg>
    <span>12 Ridgeline Avenue<br>Marlow WA 6000</span>
  </address>
  <p class="tagline">BALANCE - STRENGTH - FLEXIBILITY</p>
</section>

</body>
</html>
```